Fence Contractor Website Design

We are working with Yardline Works. They are a local fencing and automatic gate installer and in need of a new website design.
Some sites to use for inspiration:
https://pinevalebarrier.example
https://marwickrails.example
https://www.tellurpostsandboards.example
https://www.grovanpaneling.example
Thank you for taking the time to consider designing a website for us. We are web developers based in Stockton, CA, USA. Most of our projects go through the same process. Understanding this process may help you win a project with us. We custom-code all of our websites in-house. We don’t have any requirements as to what tools you use for your design, but we prefer Figma files. For any design that we label as four-stars, we send it to the client for review. The client picks the final design they want us to use. Once we complete this process, we will continue to show additional clients all the four-star sites and purchase them later. Your designs will have multiple chances to sell. For better chances of success, we ask that you follow these guidelines.
IMAGES:
If you use any images or icons in the design, we ask that you have a link to the asset so we can purchase the image/icon. Most of the designs we submit do not have the customer’s images on them unless they have some great images. Be creative; show us the feeling you are trying to portray with your image choices. Use any royalty-free site you choose. We subscribe to Stockvane and mainly use their images, but we can purchase images outside of Stockvane.
PLEASE NOTE: we will not submit designs to clients with watermarks on the images.
FONTS:
We ask that you identify the fonts used in the design. This can be done in a message if you want. We typically use Google Fonts and Stockvane Fonts.
CONTENT:
We're always open to different content and ideas. We often submit designs with stock images so the client can see our vision. We typically take pictures after the website launch to use their images with our vision. Lorem Ipsum is fine for paragraphs, but we ask that you write the headers in correct English. We want to be able to show the vision and identify the sections of the website.
INSPIRATION:
We typically add a couple of links in the brief of websites we like to help you get started in your design.
REVISIONS:
We do not often ask for revisions of the designs unless we see something in the design that may not appeal to the client. If there are slight changes that we want to make, we do that in the development process.
FEEDBACK:
We rarely give feedback on designs during the design process. We are working on many website projects and do not have the time to provide feedback. We usually respond if your request is well thought out and asks specific questions, but a note asking “feedback, please” usually goes unanswered.
Number of Pages Required
1 page
Look and feel
Each slider illustrates characteristics of the customer's brand and the style your logo design should communicate.

```html
<!DOCTYPE html>
<html lang="en">
<head>
<meta charset="utf-8">
<title>Yardline Works — Fencing &amp; Automatic Gates</title>
<link href="https://fonts.googleapis.com/css2?family=Inter:ital,wght@0,400;0,500;0,600;0,700;1,400&family=Playfair+Display:wght@600;700&display=swap" rel="stylesheet">
<style>
:root{
  --canvas:#dcdcdc;
  --blue:#1e3a9c;
  --blue-deep:#1a3290;
  --blue-bright:#2444b2;
  --red:#d42a2a;
  --ink:#1e3a9c;
  --text:#4a5060;
  --muted:#7a8090;
  --light:#f6f8fb;
  --white:#ffffff;
  --line:#dfe3ea;
  --footer:#1f1f1f;
}
*{box-sizing:border-box;margin:0;padding:0}
html,body{width:1200px;height:1200px;overflow:hidden}
body{background:var(--canvas);font-family:"Inter",sans-serif;color:var(--text);position:relative}
.page{position:absolute;left:408px;top:0;width:1112px;height:3864px;transform:scale(0.3105);transform-origin:0 0;background:var(--white);overflow:hidden}
section,header,footer{position:relative;width:100%}
.abs{position:absolute}
.serif{font-family:"Playfair Display",serif;font-weight:700}
.center{left:0;right:0;text-align:center}

/* nav */
.nav{height:42px;background:#f7f8fa;border-bottom:1px solid var(--line)}
.brand{left:220px;top:11px;display:flex;align-items:center;gap:6px;font-size:10px;font-weight:700;color:var(--blue)}
.brand-dot{width:18px;height:18px;border-radius:50%;background:var(--blue)}
.nav-links{left:330px;top:8px;display:flex;gap:14px;font-size:10px;font-weight:500;color:#333}
.nav-links a{display:block;padding:7px 12px;border-radius:6px;text-decoration:none;color:#333;position:relative}
.nav-links a.active{background:#e3e8f5;color:var(--blue)}
.nav-links a.active::after{content:"";position:absolute;left:50%;bottom:1px;width:12px;height:2px;margin-left:-6px;background:var(--red)}
.nav-cta{left:802px;top:0;width:104px;height:32px;border-radius:6px;background:var(--blue);color:#fff;font-size:10px;font-weight:600;display:flex;align-items:center;justify-content:center}

/* hero */
.hero{height:600px;background:linear-gradient(180deg,#34469a 0%,#2c45a6 55%,#2444b2 100%)}
.hero-photo{inset:0;background:linear-gradient(90deg,rgba(20,30,80,.35) 0%,rgba(40,60,150,0) 30%,rgba(40,60,150,0) 70%,rgba(20,30,80,.35) 100%)}
.hero-title{top:148px;font-size:48px;line-height:50px;color:#fff}
.hero-sub{top:262px;font-size:13px;color:#fff}
.stats{top:300px;left:0;right:0;display:flex;justify-content:center;gap:28px;color:#fff;text-align:center}
.stat b{display:block;font-size:20px;font-weight:700;line-height:26px}
.stat span{font-size:8px;opacity:.9}
.hero-btns{top:362px;left:0;right:0;display:flex;justify-content:center;gap:30px}
.btn{height:38px;padding:0 20px;border-radius:5px;font-size:10px;font-weight:600;color:#fff;display:flex;align-items:center}
.btn-outline{border:2px solid #fff}

/* section headings */
.sec-title{top:68px;font-size:28px;color:var(--ink)}
.sec-intro{top:112px;font-size:12px;line-height:19px;color:var(--text)}
.sec-intro p{width:380px;margin:0 auto}

/* services */
.services{height:754px;background:var(--light)}
.svc-grid{left:206px;top:204px;width:700px;display:grid;grid-template-columns:repeat(3,216px);gap:24px 26px}
.card{background:#fff;border-radius:8px;box-shadow:0 2px 8px rgba(20,30,70,.06);text-align:center}
.svc{height:234px;padding:28px 18px 0}
.svc-icon{width:48px;height:48px;border-radius:50%;background:var(--blue);margin:0 auto;display:flex;align-items:center;justify-content:center}
.svc h3{margin-top:18px;font-size:15px;font-weight:700;color:var(--blue)}
.svc p{margin-top:10px;font-size:10px;line-height:15.5px;color:var(--text)}
.learn{display:block;margin-top:10px;font-size:10px;font-weight:600;color:var(--red)}

/* why */
.why{height:668px;background:#fff}
.why-title{left:206px;top:66px;width:350px;font-size:24px;line-height:32px;white-space:nowrap;color:var(--ink)}
.why-text{left:206px;top:116px;width:330px;font-size:12px;line-height:19px}
.why-list{left:206px;top:192px;list-style:none;font-size:11px;color:#333}
.why-list li{display:flex;align-items:center;gap:10px;height:29px}
.tick{width:15px;height:15px;border-radius:50%;background:var(--blue);display:flex;align-items:center;justify-content:center}
.why-photo{left:574px;top:64px;width:332px;height:300px;border-radius:8px;background:linear-gradient(160deg,#c9a2a0 0%,#a5836c 35%,#6f6a3c 65%,#3a3322 100%);box-shadow:0 6px 16px rgba(0,0,0,.15);overflow:hidden}
.why-photo::after{content:"";position:absolute;inset:0;background:linear-gradient(180deg,rgba(0,0,0,0) 50%,rgba(0,0,0,.6) 100%)}
.photo-cap{position:absolute;left:18px;bottom:18px;z-index:1;color:#fff}
.photo-cap b{display:block;font-size:15px;font-weight:600}
.photo-cap span{display:block;margin-top:8px;font-size:10px;line-height:17px;width:290px}
.mini-grid{left:206px;top:416px;display:grid;grid-template-columns:160px 160px;gap:12px;}
.mini{height:90px;border-radius:4px;position:relative;overflow:hidden}
.mini::after{content:"";position:absolute;inset:0;background:linear-gradient(180deg,rgba(0,0,0,0) 35%,rgba(0,0,0,.55) 100%)}
.mini-cap{position:absolute;left:0;right:0;bottom:10px;text-align:center;color:#fff;z-index:1}
.mini-cap b{display:block;font-size:8px;font-weight:600}
.mini-cap span{display:block;font-size:6.5px;opacity:.85;margin-top:3px}

/* gallery */
.gallery{height:674px;background:var(--light)}
.filters{top:186px;left:0;right:0;display:flex;justify-content:center;gap:12px}
.pill{height:24px;padding:0 14px;border:1.5px solid var(--blue);border-radius:12px;font-size:7.5px;color:var(--blue);display:flex;align-items:center}
.pill.on{background:var(--blue);color:#fff}
.gal-grid{left:206px;top:234px;width:700px;display:grid;grid-template-columns:repeat(3,222px);gap:18px 17px}
.shot{height:182px;border-radius:6px}

/* testimonials */
.reviews{height:472px;background:#fff}
.rev-grid{left:206px;top:186px;width:700px;display:grid;grid-template-columns:repeat(3,216px);gap:26px}
.rev{height:224px;background:var(--light);border-radius:8px;position:relative;padding:22px 18px 0;text-align:center}
.quote{position:absolute;left:16px;top:12px;font-family:"Playfair Display",serif;font-size:22px;color:var(--blue)}
.stars{font-size:10px;color:var(--red);letter-spacing:3px}
.rev p{margin-top:14px;font-size:10px;line-height:17px;font-style:italic;color:#555}
.rev b{display:block;margin-top:14px;font-size:9.5px;color:var(--blue)}
.rev small{display:block;margin-top:4px;font-size:7.5px;color:var(--muted)}

/* cta */
.cta{height:590px;background:linear-gradient(180deg,var(--blue) 0%,var(--blue-bright) 100%);color:#fff}
.cta-title{left:206px;top:64px;font-size:28px}
.cta-text{left:206px;top:118px;width:330px;font-size:12px;line-height:19px}
.contacts{left:206px;top:190px;list-style:none;font-size:11px}
.contacts li{display:flex;align-items:center;gap:10px;height:29px}
.ci{width:14px;height:14px;border-radius:50%;background:var(--red);display:flex;align-items:center;justify-content:center}
.form{left:574px;top:62px;width:332px;height:464px;background:#fff;border-radius:8px;padding:22px 24px;color:var(--blue)}
.form h4{font-size:11px;font-weight:700;color:#222}
.field{margin-top:12px}
.field:first-of-type{margin-top:4px}
.field label{display:block;font-size:8.5px;font-weight:600;color:var(--blue)}
.input{margin-top:10px;height:28px;border:1px solid #c9ced8;border-radius:4px;font-size:8.5px;color:#333;padding:0 12px;display:flex;align-items:center;justify-content:space-between}
.input.area{height:72px;align-items:flex-start;padding-top:10px;color:#888}

footer{height:64px;background:var(--footer);color:#ddd;font-size:9px;display:flex;align-items:center;justify-content:center}
</style>
</head>
<body>
<div class="page">

  <header class="nav">
    <div class="abs brand"><span class="brand-dot"></span>Yardline Works</div>
    <nav class="abs nav-links">
      <a class="active">Home</a><a>Services</a><a>Gallery</a><a>Testimonials</a><a>Contact</a>
    </nav>
    <div class="abs nav-cta">Get Free Quote</div>
  </header>

  <section class="hero">
    <div class="abs hero-photo" role="img" aria-label="City street lined with tall buildings, tinted blue"></div>
    <h1 class="abs center serif hero-title">Professional Fencing &amp;<br>Automatic Gates</h1>
    <p class="abs center hero-sub">Enhancing Security and Beauty for Stockton Homes Since 1995</p>
    <div class="abs stats">
      <div class="stat"><b>25+</b><span>Years Experience</span></div>
      <div class="stat"><b>500+</b><span>Happy Customers</span></div>
      <div class="stat"><b>100%</b><span>Satisfaction</span></div>
    </div>
    <div class="abs hero-btns">
      <div class="btn">Get Free Quote</div>
      <div class="btn btn-outline">Our Services</div>
    </div>
  </section>

  <section class="services">
    <h2 class="abs center serif sec-title">Our Expert Services</h2>
    <div class="abs center sec-intro"><p>From custom fencing solutions to state-of-the-art automatic gates, we provide comprehensive services to protect and beautify your property.</p></div>
    <div class="abs svc-grid">
      <div class="card svc">
        <div class="svc-icon"><svg width="20" height="20" viewBox="0 0 20 20"><rect x="3" y="5" width="3" height="12" fill="#f2b24a"/><rect x="8.5" y="3" width="3" height="14" fill="#f2b24a"/><rect x="14" y="5" width="3" height="12" fill="#f2b24a"/><rect x="2" y="8" width="16" height="2" fill="#c9822a"/></svg></div>
        <h3>Fencing Installation</h3>
        <p>Professional installation of wood, vinyl, chain-link, and ornamental fences. Custom designs tailored to your property's needs and local regulations.</p>
        <span class="learn">Learn More →</span>
      </div>
      <div class="card svc">
        <div class="svc-icon"><svg width="20" height="20" viewBox="0 0 20 20"><rect x="6" y="2" width="8" height="16" rx="1.5" fill="#e8a33c"/><rect x="7.5" y="4" width="5" height="10" fill="#3a2a12"/></svg></div>
        <h3>Automatic Gates</h3>
        <p>State-of-the-art automatic gate systems with remote control, keypad entry, and smartphone integration for maximum convenience and security.</p>
        <span class="learn">Learn More →</span>
      </div>
      <div class="card svc">
        <div class="svc-icon"><svg width="20" height="20" viewBox="0 0 20 20"><path d="M4 16 L14 6" stroke="#fff" stroke-width="2.2" stroke-linecap="round"/><circle cx="15" cy="5" r="2.5" fill="none" stroke="#fff" stroke-width="1.6"/></svg></div>
        <h3>Maintenance &amp; Repair</h3>
        <p>Regular maintenance services and prompt repairs to keep your fencing and gates in perfect working condition year-round.</p>
        <span class="learn">Learn More →</span>
      </div>
      <div class="card svc">
        <div class="svc-icon"><svg width="20" height="20" viewBox="0 0 20 20"><rect x="5" y="3" width="10" height="14" rx="1" fill="#f1e6cf"/><rect x="7.5" y="2" width="5" height="3" fill="#b9863a"/><path d="M7 9h6M7 12h6M7 15h4" stroke="#8a7a60" stroke-width="1"/></svg></div>
        <h3>Free Consultations</h3>
        <p>Complimentary on-site consultations to assess your needs, provide expert recommendations, and deliver detailed project estimates.</p>
        <span class="learn">Learn More →</span>
      </div>
    </div>
  </section>

  <section class="why">
    <h2 class="abs serif why-title">Why Choose Yardline Works?</h2>
    <p class="abs why-text">With over 25 years of experience serving the Stockton community, we've built our reputation on quality craftsmanship, reliable service, and customer satisfaction.</p>
    <ul class="abs why-list">
      <li><span class="tick"><svg width="9" height="9" viewBox="0 0 10 10"><path d="M2 5.2l2 2 4-4.4" stroke="#fff" stroke-width="1.6" fill="none"/></svg></span>Licensed &amp; Insured Professionals</li>
      <li><span class="tick"><svg width="9" height="9" viewBox="0 0 10 10"><path d="M2 5.2l2 2 4-4.4" stroke="#fff" stroke-width="1.6" fill="none"/></svg></span>Local Stockton Expertise</li>
      <li><span class="tick"><svg width="9" height="9" viewBox="0 0 10 10"><path d="M2 5.2l2 2 4-4.4" stroke="#fff" stroke-width="1.6" fill="none"/></svg></span>Quality Materials &amp; Workmanship</li>
      <li><span class="tick"><svg width="9" height="9" viewBox="0 0 10 10"><path d="M2 5.2l2 2 4-4.4" stroke="#fff" stroke-width="1.6" fill="none"/></svg></span>Competitive Pricing &amp; Free Estimates</li>
      <li><span class="tick"><svg width="9" height="9" viewBox="0 0 10 10"><path d="M2 5.2l2 2 4-4.4" stroke="#fff" stroke-width="1.6" fill="none"/></svg></span>Warranty on All Work</li>
      <li><span class="tick"><svg width="9" height="9" viewBox="0 0 10 10"><path d="M2 5.2l2 2 4-4.4" stroke="#fff" stroke-width="1.6" fill="none"/></svg></span>Timely Project Completion</li>
    </ul>
    <div class="abs why-photo" role="img" aria-label="Sunlit cactus plants in a warm desert glow">
      <div class="photo-cap"><b>Professional Installation</b><span>Our experienced team ensures every project meets the highest standards of quality and craftsmanship.</span></div>
    </div>
    <div class="abs mini-grid">
      <div class="mini" role="img" aria-label="Birds over a pale sunset sea" style="background:linear-gradient(180deg,#e9c8b0 0%,#d7a486 60%,#8e6a58 100%)"><div class="mini-cap"><b>Quality Materials</b><span>Premium grade materials</span></div></div>
      <div class="mini" role="img" aria-label="Wide valley under a cloudy sky" style="background:linear-gradient(180deg,#5a6a7a 0%,#8b8a6a 55%,#3e3a2a 100%)"><div class="mini-cap"><b>Expert Craftsmanship</b><span>25+ years experience</span></div></div>
      <div class="mini" role="img" aria-label="Hazy city skyline seen from a hill" style="background:linear-gradient(180deg,#d0d2d2 0%,#a9aaa6 55%,#4a4844 100%)"><div class="mini-cap"><b>Local Expertise</b><span>Stockton area specialists</span></div></div>
      <div class="mini" role="img" aria-label="Golden hillside at dusk" style="background:linear-gradient(160deg,#8a7a4a 0%,#b89a4e 45%,#3a3420 100%)"><div class="mini-cap"><b>100% Satisfaction</b><span>Guaranteed results</span></div></div>
    </div>
  </section>

  <section class="gallery">
    <h2 class="abs center serif sec-title">Our Work Speaks for Itself</h2>
    <div class="abs center sec-intro"><p style="width:360px">Browse through our portfolio of completed projects showcasing our commitment to quality and attention to detail.</p></div>
    <div class="abs filters">
      <span class="pill on">All Projects</span><span class="pill">Fencing</span><span class="pill">Gates</span><span class="pill">Before/After</span>
    </div>
    <div class="abs gal-grid">
      <div class="shot" role="img" aria-label="Project photo with warm fiery light in a dark setting" style="background:linear-gradient(120deg,#2a1a14 0%,#5a3222 40%,#d98a3a 70%,#3a2218 100%)"></div>
      <div class="shot" role="img" aria-label="Project photo with warm fiery light in a dark setting" style="background:linear-gradient(120deg,#2a1a14 0%,#5a3222 40%,#d98a3a 70%,#3a2218 100%)"></div>
      <div class="shot" role="img" aria-label="Green field under a stormy grey sky" style="background:linear-gradient(180deg,#5c6670 0%,#8a949a 45%,#5a8a3a 62%,#3f7a2a 100%)"></div>
      <div class="shot" role="img" aria-label="Meadow of dandelions under a bright sky" style="background:linear-gradient(180deg,#b8c6d2 0%,#e3e6e2 40%,#7a8a5a 65%,#3a4a22 100%)"></div>
      <div class="shot" role="img" aria-label="Close-up of dark metal machinery parts" style="background:linear-gradient(135deg,#1a1a1e 0%,#55525a 40%,#24222a 70%,#6a6670 100%)"></div>
      <div class="shot" role="img" aria-label="Narrow stone alley opening toward the sea" style="background:linear-gradient(90deg,#4a3e34 0%,#8a7c6a 35%,#a9b4bc 55%,#5e5446 100%)"></div>
    </div>
  </section>

  <section class="reviews">
    <h2 class="abs center serif sec-title">What Our Customers Say</h2>
    <div class="abs center sec-intro"><p style="width:360px">Don't just take our word for it - hear from satisfied customers throughout Stockton and surrounding areas.</p></div>
    <div class="abs rev-grid">
      <div class="rev"><span class="quote">"</span><div class="stars">★★★★★</div>
        <p>Yardline Works transformed our backyard with a beautiful custom fence. The installation was professional, timely, and exceeded our expectations. Highly recommend their services!</p>
        <b>Dana Whitlow</b><small>Stockton, CA</small></div>
      <div class="rev"><span class="quote">"</span><div class="stars">★★★★★</div>
        <p>Our new automatic gate works flawlessly and adds so much convenience to our daily routine. The team was knowledgeable and completed the project ahead of schedule.</p>
        <b>Marco Ellison</b><small>Lodi, CA</small></div>
      <div class="rev"><span class="quote">"</span><div class="stars">★★★★★</div>
        <p>Excellent customer service from start to finish. They provided a detailed estimate, kept us informed throughout the process, and the final result is exactly what we envisioned.</p>
        <b>Lena Park</b><small>Manteca, CA</small></div>
    </div>
  </section>

  <section class="cta">
    <h2 class="abs serif cta-title">Ready to Get Started?</h2>
    <p class="abs cta-text">Contact Yardline Works today for a free consultation and estimate. We're here to help you enhance your property's security and curb appeal.</p>
    <ul class="abs contacts">
      <li><span class="ci"><svg width="8" height="8" viewBox="0 0 10 10"><path d="M5 1a3 3 0 0 1 3 3c0 2.2-3 5-3 5S2 6.2 2 4a3 3 0 0 1 3-3z" fill="#fff"/></svg></span>418 Alder Row, Stockton, CA 95202</li>
      <li><span class="ci"><svg width="8" height="8" viewBox="0 0 10 10"><path d="M2 1.5l2 .3.6 2-1.2.9a6 6 0 0 0 2.5 2.5l.9-1.2 2 .6.3 2C6 9 1 4 2 1.5z" fill="#fff"/></svg></span>(209) 555-0187</li>
      <li><span class="ci"><svg width="8" height="8" viewBox="0 0 10 10"><rect x="1" y="2.5" width="8" height="5.5" rx=".6" fill="#fff"/><path d="M1.3 2.8L5 5.6l3.7-2.8" stroke="#d42a2a" stroke-width=".8" fill="none"/></svg></span>hello@yardlineworks.example</li>
      <li><span class="ci"><svg width="8" height="8" viewBox="0 0 10 10"><circle cx="5" cy="5" r="3.6" fill="#fff"/><path d="M5 3v2.2l1.4.9" stroke="#d42a2a" stroke-width=".9" fill="none"/></svg></span>Mon-Fri: 8AM-6PM, Sat: 9AM-4PM</li>
    </ul>
    <div class="abs form">
      <h4>Get Your Free Quote</h4>
      <div class="field"><label>Full Name *</label><div class="input"></div></div>
      <div class="field"><label>Email Address *</label><div class="input"></div></div>
      <div class="field"><label>Phone Number *</label><div class="input"></div></div>
      <div class="field"><label>Service Needed</label><div class="input">Select a service<svg width="8" height="6" viewBox="0 0 8 6"><path d="M1 1.5l3 3 3-3" stroke="#333" stroke-width="1.2" fill="none"/></svg></div></div>
      <div class="field"><label>Project Details</label><div class="input area">Tell us about your project needs...</div></div>
    </div>
  </section>

  <footer>© 2024 Yardline Works. All rights reserved. | Licensed &amp; Insured | Serving Stockton, CA and Surrounding Areas</footer>

</div>
</body>
</html>
```